Maple Grove Schools | brand new stationery!

We need stationery design with our new logo! Our company updated it's name and image and we like to incorporate the new one on our stationery, business cards and email signature. We are looking for fresh, new ideas!
Industry: Childcare, Elementary and Middle School
Company Name: Maple Grove Schools
Tagline: Bright Futures Start Here
Main colors: Blue, white and a little yellow
Star shape is something new for us! Do you see a way to incorporate it as a design element?

```html
<!DOCTYPE html>
<html lang="en">
<head>
<meta charset="utf-8">
<title>Maple Grove Schools — Stationery</title>
<link rel="stylesheet" href="https://fonts.googleapis.com/css2?family=Outfit:wght@400;600&family=Mulish:wght@400&display=swap">
<style>
  :root {
    --navy: #252a6b;
    --yellow: #fdc116;
    --paper: #f2f2f4;
    --stage: #d1d2d4;
    --ink: #3b3d4a;
    --white: #ffffff;
  }
  * { margin: 0; padding: 0; box-sizing: border-box; }
  html, body { width: 1200px; height: 851px; overflow: hidden; }
  body { background: var(--stage); position: relative; font-family: "Mulish", sans-serif; color: var(--ink); }

  .card { position: absolute; background: var(--paper); overflow: hidden; }
  .card--front { left: 90px; top: 80px; width: 499px; height: 288px; }
  .card--back { left: 613px; top: 80px; width: 499px; height: 288px; background: var(--navy); }
  .card--signature { left: 90px; top: 473px; width: 1029px; height: 294px; }

  .corner { position: absolute; left: 0; top: 0; width: 126px; height: 101px; }
  .corner polygon { fill: var(--yellow); }

  .brand-name { font-family: "Outfit", sans-serif; font-weight: 600; color: var(--navy); line-height: 1; }
  .brand-name span { display: block; }

  .card--front .brand-name { position: absolute; right: 32px; top: 28px; text-align: center; font-size: 33px; }
  .card--front .brand-name span + span { font-size: 29px; margin-top: 3px; }
  .brand-disc { position: absolute; border-radius: 50%; background: var(--navy); }
  .card--front .brand-disc { left: 320px; top: 146px; width: 108px; height: 108px; }

  .contact-list { list-style: none; position: absolute; }
  .contact-list li { display: flex; align-items: center; white-space: nowrap; }
  .contact-list svg { flex: none; fill: var(--navy); }
  .contact-list .accent { color: var(--yellow); }
  .card--front .contact-list { left: 40px; top: 163px; font-size: 12px; }
  .card--front .contact-list li { height: 18px; }
  .card--front .contact-list svg { width: 10px; height: 10px; margin-right: 13px; }
  .address { position: absolute; line-height: 1.55; }
  .card--front .address { left: 40px; top: 243px; font-size: 12px; }

  .card--back .brand-disc { left: 218px; top: 64px; width: 62px; height: 62px; background: var(--white); }
  .card--back .brand-name { position: absolute; left: 0; right: 0; top: 137px; text-align: center; color: var(--white); font-size: 33px; }
  .card--back .brand-name span + span { font-size: 29px; margin-top: 3px; }

  .card--signature .brand-name.large { position: absolute; left: 110px; top: 111px; font-size: 50px; }
  .card--signature .brand-name.large span + span { font-size: 44px; margin-top: 2px; }
  .divider { position: absolute; left: 541px; top: 92px; width: 2px; height: 115px; background: var(--navy); }
  .card--signature .address { left: 660px; top: 82px; font-size: 15px; }
  .card--signature .contact-list { left: 660px; top: 146px; font-size: 15px; }
  .card--signature .contact-list li { height: 23px; }
  .card--signature .contact-list svg { width: 13px; height: 13px; margin-right: 17px; }
  .signature-mark { position: absolute; left: 870px; top: 181px; width: 140px; text-align: center; }
  .signature-mark .brand-disc { position: static; display: block; margin: 0 auto 7px; width: 40px; height: 40px; }
  .signature-mark .brand-name { font-size: 20px; color: #1f2033; }
</style>
</head>
<body>
<svg width="0" height="0" style="position:absolute" aria-hidden="true">
  <symbol id="icon-phone" viewBox="0 0 16 16"><path d="M3.5 1l2.6 3-1.4 1.8c.9 2 2.6 3.7 4.6 4.6L11 9l3 2.6-1.5 2.6C7 14 2 9 1.8 3.5z"/></symbol>
  <symbol id="icon-mail" viewBox="0 0 16 16"><path d="M1 3h14v10H1zm1.5 1.2L8 8.6l5.5-4.4z" fill-rule="evenodd"/></symbol>
  <symbol id="icon-globe" viewBox="0 0 16 16"><circle cx="8" cy="8" r="7"/><path d="M5 4c2 0 2 2 4 2s1 3-1 3-2 3-3 2-1-5 0-7z" fill="#f2f2f4"/></symbol>
</svg>

<section class="card card--front" aria-label="Business card front">
  <svg class="corner" viewBox="0 0 126 101" aria-hidden="true"><polygon points="0,0 126,0 0,101"/></svg>
  <h1 class="brand-name"><span>Maple Grove</span><span>Schools</span></h1>
  <ul class="contact-list">
    <li><svg><use href="#icon-phone"/></svg>555 (0) 010 234 567</li>
    <li><svg><use href="#icon-mail"/></svg>hi.maple(@)grove.ca</li>
    <li><svg><use href="#icon-globe"/></svg>www.<span class="accent">maplegrove</span>.ca</li>
  </ul>
  <p class="address">Po box 1780 linden<br>riverton, ab t0-1k3</p>
  <div class="brand-disc" aria-hidden="true"></div>
</section>

<section class="card card--back" aria-label="Business card back">
  <div class="brand-disc" aria-hidden="true"></div>
  <h2 class="brand-name"><span>Maple Grove</span><span>Schools</span></h2>
</section>

<section class="card card--signature" aria-label="Email signature">
  <svg class="corner" viewBox="0 0 126 101" aria-hidden="true"><polygon points="0,0 126,0 0,101"/></svg>
  <h2 class="brand-name large"><span>Maple Grove</span><span>Schools</span></h2>
  <div class="divider" aria-hidden="true"></div>
  <p class="address">Po box 1780 linden<br>riverton, ab t0-1k3</p>
  <ul class="contact-list">
    <li><svg><use href="#icon-phone"/></svg>555 (0) 010 234 567</li>
    <li><svg><use href="#icon-mail"/></svg>hi.maple(@)grove.ca</li>
    <li><svg><use href="#icon-globe"/></svg>www.<span class="accent">maplegrove</span>.ca</li>
  </ul>
  <div class="signature-mark">
    <div class="brand-disc" aria-hidden="true"></div>
    <p class="brand-name"><span>Maple Grove</span><span>Schools</span></p>
  </div>
</section>
</body>
</html>
```